Recruitment Flyer for Harbourline Home Loan company

Harbourline Home Loan centre requires a four page A4 color brochure for new staff who will be joining the organisation.

The brochure is received during the interview for the job role. so we are looking for nice glossy pictures combined with sufficient text to enable the applicant to make an informed decision.

I have attached a word document that may help plus lots of pictures that are on the website that could be used also.

Target Market(s)

New staff joining the organisation

Industry/Entity Type

Mortgage

Font styles to use
Sans Serif

Colors
3377b5
6b449b
b768aa
34a6d7

Requirements
Must have
• Glossy, colorful and career happy
Nice to have
• lots of photos and opportunity for text
Should not have
• be sad or not happy

```html
<!DOCTYPE html>
<html lang="en">
<head>
<meta charset="utf-8">
<title>Harbourline Home Loan Centre – Brochure Cover</title>
<link rel="stylesheet" href="https://fonts.googleapis.com/css2?family=Lato:wght@400;700;900&display=swap">
<style>
  :root {
    --backdrop: #dcdcdc;
    --paper: #ffffff;
    --cyan: #1fb8e6;
    --cyan-light: #5fd0f2;
    --blue: #3377b5;
    --purple: #5b2a92;
    --violet: #b768aa;
    --ink: #3a3a3a;
    --photo-warm: #c9a27c;
    --photo-light: #efe4d6;
  }
  * { box-sizing: border-box; margin: 0; padding: 0; }
  html, body { width: 1200px; height: 765px; overflow: hidden; }
  body {
    background: var(--backdrop);
    font-family: "Lato", Arial, sans-serif;
    color: var(--ink);
  }
  .spread {
    position: absolute;
    left: 105px; top: 32px;
    width: 990px; height: 700px;
    display: flex;
    box-shadow: 0 6px 24px rgba(0,0,0,.18);
  }
  .page {
    position: relative;
    width: 495px; height: 700px;
    background: var(--paper);
    overflow: hidden;
  }
  .page svg.shapes { position: absolute; inset: 0; }

  /* back cover */
  .back-cover .top-band {
    position: absolute; left: 0; top: 0; width: 100%; height: 14px;
    background: var(--cyan);
  }
  .brand {
    display: flex; align-items: center; gap: 10px;
    color: var(--cyan);
    font-weight: 700;
    text-transform: uppercase;
    letter-spacing: .5px;
  }
  .brand .mark {
    border-radius: 50%;
    background: var(--violet);
    flex: none;
  }
  .back-cover .brand {
    position: absolute; left: 120px; top: 250px;
    font-size: 19px; line-height: 1.1;
  }
  .back-cover .brand .mark { width: 44px; height: 44px; }
  .contact {
    position: absolute; left: 160px; top: 310px;
    font-weight: 700; font-size: 19px; line-height: 1.45;
    color: var(--ink);
  }
  .contact .web { letter-spacing: 4px; }

  /* front cover */
  .front-cover .brand {
    position: absolute; left: 0; right: 0; top: 20px;
    justify-content: center;
    font-size: 17px; line-height: 1.1;
  }
  .front-cover .brand .mark { width: 34px; height: 34px; }
  .photo {
    position: absolute; left: 0; top: 74px; width: 100%; height: 300px;
    background: linear-gradient(160deg, var(--photo-light) 0%, var(--photo-warm) 70%, #a98462 100%);
  }
  .badge {
    position: absolute; left: 370px; top: 255px;
    width: 112px; height: 112px; border-radius: 50%;
    background: var(--paper);
    border: 3px solid var(--purple);
    box-shadow: 0 0 0 4px var(--paper), 0 0 0 6px var(--violet);
    display: flex; flex-direction: column; align-items: center; justify-content: center;
    text-align: center; color: var(--purple);
  }
  .badge .big { font-weight: 900; font-size: 24px; line-height: 1; }
  .badge .label { font-weight: 900; font-size: 15px; letter-spacing: .5px; }
  .badge .small { font-size: 8px; line-height: 1.2; color: var(--ink); margin-top: 3px; width: 70px; }
  .headline {
    position: absolute; left: 90px; top: 420px; width: 390px;
    color: var(--paper);
  }
  .headline h1 { font-weight: 700; font-size: 48px; line-height: 1; }
  .headline .sub { font-weight: 700; font-size: 17px; margin-top: 6px; }
  .headline .call { color: var(--purple); font-weight: 700; font-size: 19px; margin-top: 8px; }
  .front-cover .web {
    position: absolute; left: 0; right: 0; bottom: 22px;
    text-align: center; font-weight: 700; font-size: 16px; letter-spacing: 4px;
  }
</style>
</head>
<body>
  <main class="spread">
    <section class="page back-cover">
      <div class="top-band"></div>
      <svg class="shapes" viewBox="0 0 495 700" aria-hidden="true">
        <path d="M495 460 C 340 470 200 560 130 700 L 495 700 Z" fill="var(--violet)"/>
        <path d="M495 478 C 350 490 225 575 165 700 L 495 700 Z" fill="var(--purple)"/>
        <path d="M495 500 C 365 512 250 590 200 700 L 495 700 Z" fill="var(--cyan)"/>
        <path d="M495 610 C 420 620 360 660 335 700 L 495 700 Z" fill="var(--paper)"/>
      </svg>
      <div class="brand"><span class="mark"></span><span>Harbourline<br>Home Loan Centre</span></div>
      <div class="contact">
        <p>CALL US: 123 456 7890</p>
        <p>lorem@lorem ipsum</p>
        <p class="web">www.lorem.com</p>
      </div>
    </section>

    <section class="page front-cover">
      <div class="brand"><span class="mark"></span><span>Harbourline<br>Home Loan Centre</span></div>
      <div class="photo" role="img" aria-label="Photo of a smiling family of four unpacking moving boxes in their new home"></div>
      <svg class="shapes" viewBox="0 0 495 700" aria-hidden="true">
        <path d="M0 400 C 120 300 300 255 495 248 L 495 640 L 0 640 Z" fill="var(--violet)"/>
        <path d="M0 412 C 125 312 305 268 495 262 L 495 640 L 0 640 Z" fill="var(--purple)"/>
        <path d="M0 430 C 130 330 310 284 495 278 L 495 640 L 0 640 Z" fill="var(--cyan)"/>
        <path d="M0 640 L 495 640 L 495 700 L 0 700 Z" fill="var(--paper)"/>
      </svg>
      <div class="badge">
        <span class="big">100%</span>
        <span class="label">GARANTEE</span>
        <span class="small">Lorem Ipsum is simply dummy text</span>
      </div>
      <div class="headline">
        <h1>Lorem Ipsum</h1>
        <p class="sub">is simply dummy text of the printing</p>
        <p class="call">CALL US: 123 456 7890</p>
      </div>
      <p class="web">www.lorem.com</p>
    </section>
  </main>
</body>
</html>
```